Vorn Solutions: searching for a flyer to trow in letterboxes for properties we are interested in

Hello ,

Introduction:
We are a company based in Luxembourg called "Vorn Solutions". We are specialized in buying properties on which we develop and build constructions before selling them.

Informations for the flyer:
We need a flyer to trow into the letter boxes of property owners letting them know that we are interested in buying their property, if they are interested they can give us a call.

The text for the flyer/letter is in the attachment called >>2020-03-11_VS_Text for flyer,letter there might be slight changes<<.

We need to look competent, professional and financially stable.

The flyer needs to be short and not over welling with information otherwise it will land in the trash.

We have decided that we don't want real pictures on the flyer, but shapes of any kind, blue prints, drawings are fine.

Format should be in DIN A4. We plan to print the flyer on both sides in two different languages, in other words the design will be the same on both sides only the text will be in a different language.

I also added our current logo and here is the design of the website that is under construction at the moment http://www.vornsolutions.example/. The logo's color can be changed into a different blue or uni color (all white or all black).
Updates

Hi, First time user the howl thing started faster as expected. Furthermore, I need to catch my boss to discust the project with him and he is on a lot of meetings. Please give us a little bit more time. Thanks

Target Market(s)

Property owners

Requirements
Must have
• email, phone number, tax number (RCS), Tax number , matriculation and address.
see word file in attachment for information
Nice to have
• Our company logo, in one form or an other, you can be creative, the logo is in the attachment.
Should not have
• Real pictures

```html
<!DOCTYPE html>
<html lang="fr">
<head>
<meta charset="utf-8">
<title>Vorn Solutions – Papeterie</title>
<link href="https://fonts.googleapis.com/css2?family=Oswald:wght@600&family=Roboto:wght@400;700&family=PT+Sans:wght@400;700&display=swap" rel="stylesheet">
<style>
  :root {
    --brand-blue: #135f8e;
    --brand-blue-dark: #0c4a72;
    --ink: #1e1f22;
    --paper: #f1f2f4;
    --paper-shade: #dcdee2;
    --backdrop: #3a3d42;
    --white: #ffffff;
  }
  * { box-sizing: border-box; margin: 0; padding: 0; }
  html, body { width: 1191px; height: 1200px; overflow: hidden; }
  body { background: var(--backdrop); position: relative; font-family: "Roboto", sans-serif; color: var(--ink); }

  .letter {
    position: absolute; top: 87px; width: 521px; height: 736px;
    background: linear-gradient(160deg, var(--paper-shade) 0%, var(--paper) 35%, #fafafa 60%, var(--paper) 100%);
    overflow: hidden;
  }
  .letter--fr { left: 71px; }
  .letter--lb { left: 618px; }
  .letter__topband { position: absolute; left: 0; top: 0; width: 100%; height: 24px; background: var(--brand-blue); }
  .wordmark {
    font-family: "Oswald", sans-serif; font-weight: 600; color: var(--brand-blue);
    letter-spacing: 0.3px; white-space: nowrap; text-transform: uppercase;
  }
  .letter__wordmark { position: absolute; top: 170px; left: 0; width: 100%; text-align: center; font-size: 40px; line-height: 1; }
  .letter__illustration {
    position: absolute; left: 183px; top: 394px; width: 338px; height: 234px;
    background: radial-gradient(ellipse 60% 62% at 62% 58%, rgba(95,97,102,0.34) 0%, rgba(150,152,156,0.2) 45%, rgba(240,241,243,0) 100%);
  }
  .letter__body { position: absolute; left: 41px; top: 236px; width: 440px; font-size: 11.2px; line-height: 14.8px; }
  .letter__body p { margin-bottom: 14.6px; }
  .letter__salute { font-weight: 700; }
  .letter__signature {
    position: absolute; left: 28px; top: 422px; width: 199px; height: 62px;
    background: radial-gradient(ellipse 50% 40% at 50% 55%, rgba(19,95,142,0.12) 0%, rgba(19,95,142,0) 100%);
  }
  .letter--lb .letter__signature { top: 428px; }
  .letter__team { position: absolute; left: 41px; top: 495px; font-size: 12.2px; font-weight: 700; }
  .letter__footer { position: absolute; left: 0; top: 628px; width: 100%; height: 108px; background: var(--paper); }
  .footer__band {
    position: absolute; left: 0; top: 0; width: 409px; height: 100%;
    background: linear-gradient(120deg, var(--brand-blue-dark), var(--brand-blue));
  }
  .contact { position: absolute; left: 41px; top: 13px; font-family: "PT Sans", sans-serif; color: var(--white); font-size: 10.8px; line-height: 14.2px; text-transform: uppercase; }
  .contact__name { font-weight: 700; }
  .contact__row { position: relative; }
  .contact__icon { position: absolute; left: -14px; top: 2px; width: 10px; height: 10px; }

  .envelope { position: absolute; top: 934px; height: 226px; overflow: hidden; background: linear-gradient(160deg, var(--paper-shade), var(--paper) 45%, #fafafa); }
  .envelope--front { left: 70px; width: 522px; }
  .envelope--back { left: 605px; width: 518px; }
  .envelope__wordmark { position: absolute; top: 123px; width: 100%; text-align: center; font-size: 36px; line-height: 1; }
  .envelope__band { position: absolute; left: 0; top: 180px; width: 472px; height: 46px; background: linear-gradient(120deg, var(--brand-blue-dark), var(--brand-blue)); }
  .envelope__web { position: absolute; left: 0; top: 196px; width: 472px; text-align: center; font-family: "PT Sans", sans-serif; color: var(--white); font-size: 9.5px; letter-spacing: 4.2px; text-transform: uppercase; }
  .envelope__flap { position: absolute; left: 0; top: 0; }
  .envelope__contact { position: absolute; left: 24px; top: 120px; font-family: "PT Sans", sans-serif; font-size: 8.8px; line-height: 12.1px; text-transform: uppercase; color: var(--ink); }
  .envelope__contact .contact__name { font-weight: 700; }
  .envelope__backmark { position: absolute; left: 336px; top: 166px; font-size: 23px; line-height: 1; }
</style>
</head>
<body>

<article class="letter letter--fr" lang="fr">
  <div class="letter__topband"></div>
  <div class="wordmark letter__wordmark">Vorn Solutions</div>
  <div class="letter__illustration" role="img" aria-label="Croquis d’architecture d’un immeuble de bureaux en perspective"></div>
  <div class="letter__body">
    <p class="letter__salute">Madame, Monsieur,</p>
    <p>Ce courrier vous a été adressé, car votre propriété a attiré notre attention. Nous souhaiterions discuter avec vous de son éventuel rachat par notre société.</p>
    <p>En cas d’accord, nous vous assurons une décision rapide, un paiement garanti, et zéro frais d’intermédiaire.</p>
    <p>En attendant de vos nouvelles, nous restons à votre entière disposition pour tout renseignement.</p>
    <p>Salutations distinguées,</p>
  </div>
  <div class="letter__signature" role="img" aria-label="Signature manuscrite Vorn Solutions"></div>
  <div class="letter__team">L’équipe de Vorn Solutions</div>
  <footer class="letter__footer">
    <div class="footer__band"></div>
    <div class="contact">
      <div class="contact__name">Company name : Vorn Solutions Sàrl</div>
      <div class="contact__row"><svg class="contact__icon" viewBox="0 0 10 10"><circle cx="5" cy="5" r="5" fill="#fff"/><path d="M5 2.2a1.8 1.8 0 0 0-1.8 1.8C3.2 5.4 5 7.8 5 7.8S6.8 5.4 6.8 4A1.8 1.8 0 0 0 5 2.2z" fill="#135f8e"/></svg>Address : 18 Rue des Tilleuls, L-4100 Esch-Nord</div>
      <div class="contact__row"><svg class="contact__icon" viewBox="0 0 10 10"><circle cx="5" cy="5" r="5" fill="#fff"/><rect x="2.5" y="3.3" width="5" height="3.4" fill="#135f8e"/></svg>Email: info@vornsolutions.example</div>
      <div class="contact__row"><svg class="contact__icon" viewBox="0 0 10 10"><circle cx="5" cy="5" r="5" fill="#fff"/><path d="M3 2.6l1.2 1.2-.6.8c.4.8 1 1.4 1.8 1.8l.8-.6L7.4 7 6.6 7.8C4.6 7.6 2.4 5.4 2.2 3.4z" fill="#135f8e"/></svg>Tel. : 600 555 019</div>
      <div class="contact__row"><svg class="contact__icon" viewBox="0 0 10 10"><circle cx="5" cy="5" r="5" fill="#fff"/><rect x="3.2" y="2.6" width="3.6" height="4.8" fill="#135f8e"/></svg>RCS : B000451 &nbsp;| &nbsp;Matr : 2000 1234 567 &nbsp;| &nbsp;TVA : LU 00012345</div>
    </div>
  </footer>
</article>

<article class="letter letter--lb" lang="lb">
  <div class="letter__topband"></div>
  <div class="wordmark letter__wordmark">Vorn Solutions</div>
  <div class="letter__illustration" role="img" aria-label="Croquis d’architecture d’un immeuble de bureaux en perspective"></div>
  <div class="letter__body">
    <p class="letter__salute">Madame, Monsieur,</p>
    <p>Dir kritt dëst Schreiwes well Är Proprietéit eis Opmierksamkeet zeréckbehalen huet. Mir géinge gär mat Iech iwwert d’Méiglechkeet, datt eise Betrib se opkeeft, diskutéieren.</p>
    <p>Mir versécheren Iech e séieren Entscheedungsprozess, garantéieren d’Bezuelung a verrechne keng Drëttkäschten.</p>
    <p>Mir géingen eis freeën, vun Iech ze héieren, a sti ganz zu Ärer Verfügung fir zousätzlech Informatiounen.</p>
    <p>Mat beschte Gréiss,</p>
  </div>
  <div class="letter__signature" role="img" aria-label="Signature manuscrite Vorn Solutions"></div>
  <div class="letter__team">D’Equipe vun Vorn Solutions</div>
  <footer class="letter__footer">
    <div class="footer__band"></div>
    <div class="contact">
      <div class="contact__name">Company name : Vorn Solutions Sàrl</div>
      <div class="contact__row"><svg class="contact__icon" viewBox="0 0 10 10"><circle cx="5" cy="5" r="5" fill="#fff"/><path d="M5 2.2a1.8 1.8 0 0 0-1.8 1.8C3.2 5.4 5 7.8 5 7.8S6.8 5.4 6.8 4A1.8 1.8 0 0 0 5 2.2z" fill="#135f8e"/></svg>Address : 18 Rue des Tilleuls, L-4100 Esch-Nord</div>
      <div class="contact__row"><svg class="contact__icon" viewBox="0 0 10 10"><circle cx="5" cy="5" r="5" fill="#fff"/><rect x="2.5" y="3.3" width="5" height="3.4" fill="#135f8e"/></svg>Email: info@vornsolutions.example</div>
      <div class="contact__row"><svg class="contact__icon" viewBox="0 0 10 10"><circle cx="5" cy="5" r="5" fill="#fff"/><path d="M3 2.6l1.2 1.2-.6.8c.4.8 1 1.4 1.8 1.8l.8-.6L7.4 7 6.6 7.8C4.6 7.6 2.4 5.4 2.2 3.4z" fill="#135f8e"/></svg>Tel. : 600 555 019</div>
      <div class="contact__row"><svg class="contact__icon" viewBox="0 0 10 10"><circle cx="5" cy="5" r="5" fill="#fff"/><rect x="3.2" y="2.6" width="3.6" height="4.8" fill="#135f8e"/></svg>RCS : B000451 &nbsp;| &nbsp;Matr : 2000 1234 567 &nbsp;| &nbsp;TVA : LU 00012345</div>
    </div>
  </footer>
</article>

<section class="envelope envelope--front">
  <div class="wordmark envelope__wordmark">Vorn Solutions</div>
  <div class="envelope__band"></div>
  <div class="envelope__web">www.vornsolutions.example</div>
</section>

<section class="envelope envelope--back">
  <svg class="envelope__flap" width="518" height="70" viewBox="0 0 518 70">
    <path d="M0 0H518L494 52Q486 68 466 68H52Q32 68 24 52Z" fill="#135f8e"/>
  </svg>
  <div class="envelope__contact">
    <div class="contact__name">Company name : Vorn Solutions Sàrl</div>
    <div>Address : 18 Rue des Tilleuls, L-4100 Esch-Nord</div>
    <div>Email: info@vornsolutions.example</div>
    <div>Tel. : 600 555 019</div>
    <div>RCS : B000451 &nbsp;| &nbsp;Matr : 2000 1234 567 &nbsp;| &nbsp;TVA : LU 00012345</div>
  </div>
  <div class="wordmark envelope__backmark">Vorn Solutions</div>
</section>

</body>
</html>
```